Business Card Design

I need a business card for company that is a limited company that was originally an off-road vehicle company (atv's side by sides snowmobiles and motorcycles) and I have recently sold the assets of the company that was operating under a different name and have become semi retired. I continue to do maintenance on these types of vehicles and also sell and install parts and accessories. Recently I have also contracted to a snowmobile club to operate their groomer to groom the snowmobile trails. I would like bright and bold colors.
Industry/Entity Type
Club
Contact Information for Business Card
KWT Holdings Ltd.
Marcus Ellery
780-555-0143

```html
<!DOCTYPE html>
<html lang="en">
<head>
<meta charset="utf-8">
<title>KWT Holdings Ltd. – Business Card</title>
<link rel="stylesheet" href="https://fonts.googleapis.com/css2?family=Arimo:wght@400;700&display=swap">
<style>
  :root {
    --backdrop: #0a2d6e;
    --card-black: #000000;
    --card-yellow: #fffc00;
    --ink: #000000;
  }
  html, body {
    margin: 0;
    padding: 0;
    width: 1200px;
    height: 1000px;
    overflow: hidden;
    background: var(--backdrop);
  }
  .canvas { display: block; width: 1200px; height: 1000px; }
  .card-text { font-family: "Arimo", Helvetica, Arial, sans-serif; fill: var(--ink); }
  .company-name { font-weight: 700; font-size: 46px; letter-spacing: 1px; text-transform: uppercase; }
  .person-name { font-size: 26px; font-weight: 400; }
  .person-name .surname { font-weight: 700; }
  .credential { font-size: 15px; }
  .contact { font-size: 17px; }
  .fill-black { fill: var(--card-black); }
  .fill-yellow { fill: var(--card-yellow); }
  .divider { stroke: var(--ink); stroke-width: 2; }
</style>
</head>
<body>
<svg class="canvas" viewBox="0 0 1200 1000" xmlns="http://www.w3.org/2000/svg">
  <!-- Front of card -->
  <g class="card-front">
    <rect class="fill-black" x="291" y="107" width="617" height="361"/>
    <polygon class="fill-yellow" points="291,290 908,125 908,288 291,453"/>
    <rect class="fill-yellow" x="340" y="125" width="150" height="102" rx="20"
          role="img" aria-label="Yellow silhouette of a dirt bike motorcycle"/>
    <rect class="fill-yellow" x="696" y="348" width="182" height="90" rx="20"
          role="img" aria-label="Yellow silhouette of a snowmobile"/>
    <text class="card-text company-name" x="604" y="306" text-anchor="middle"
          textLength="560" lengthAdjust="spacingAndGlyphs"
          transform="rotate(-15 604 290)">KWT Holdings Ltd.</text>
  </g>

  <!-- Back of card -->
  <g class="card-back">
    <rect class="fill-yellow" x="291" y="510" width="617" height="362"/>
    <line class="divider" x1="540" y1="679" x2="540" y2="872"/>
    <text class="card-text person-name" x="559" y="728">Marcus <tspan class="surname">Ellery</tspan></text>
    <text class="card-text credential" x="559" y="781">Journeyman Red Seal Automotive Technician</text>
    <text class="card-text credential" x="559" y="801">Journeyman Red Seal Motorcycle Technician</text>
    <text class="card-text credential" x="559" y="821">Journeyman Parts Man</text>
    <text class="card-text contact" x="526" y="798" text-anchor="end">780.555.0143</text>
    <text class="card-text contact" x="526" y="822" text-anchor="end">kwthold.77@example.com</text>
  </g>
</svg>
</body>
</html>
```